Mobile Tutoring Service needs a Flier for Distribution to Clients

Lantern Scholars Inc. is a tutoring company that uses video call technology to perform tutoring session in math, sciences, and standardized test preparation. We need a flier that we can distribute to email lists of parents in school districts around the St. Louis Area, as well as post in public areas to attract clients. The following file has the important information needed on the flier. In particular, the "How it Works" Steps 1-3 can be made into an animation or video that looks attractive and helps potential clients understand our process. Our logo is also found in the document. Ideally, all information in the power point slide will be in the flier.

Target Market(s)

Parents for middle and high schoolers grade 6-12 in the St. Louis Area

Industry/Entity Type

Tutoring

Font styles to use
Serif

Colors
3176b5
85abd2
0492cd
33a6d7
ceeaf5

Requirements
Must have
• All the information with the attached file
Nice to have
• A nice-looking animation instead of the still screen shoots that are included in the attached file.

```html
<!DOCTYPE html>
<html lang="en">
<head>
<meta charset="utf-8">
<title>Lantern Scholars – Mobile Tutoring Flier</title>
<link href="https://fonts.googleapis.com/css2?family=Open+Sans:wght@400;600;700&display=swap" rel="stylesheet">
<style>
  :root{
    --ink-dark:#1f2226;
    --ink-footer:#2b2e31;
    --blue-deep:#1a73c2;
    --blue-mid:#0492cd;
    --blue-bright:#33a6d7;
    --blue-soft:#85abd2;
    --blue-pale:#ceeaf5;
    --paper:#f3f3f3;
    --text:#3a3a3a;
    --rule:#5d8fc9;
    --white:#ffffff;
  }
  *{margin:0;padding:0;box-sizing:border-box}
  html,body{width:1038px;height:1200px;overflow:hidden;background:var(--paper)}
  body{font-family:"Open Sans",Arial,sans-serif;color:var(--text)}
  .flier{position:relative;width:1038px;height:1200px;background:var(--paper);overflow:hidden}

  /* Hero */
  .hero{position:absolute;left:0;top:0;width:1038px;height:459px;background:var(--ink-dark)}
  .hero-photo{position:absolute;left:0;top:0}
  .brand{position:absolute;left:14px;top:184px;display:flex;align-items:center;gap:14px}
  .brand-dot{width:28px;height:28px;border-radius:50%;background:var(--blue-deep);flex:none}
  .brand-name{font-weight:700;font-size:34px;line-height:46px;color:var(--white);letter-spacing:-0.5px}
  .brand-rule{position:absolute;left:30px;top:249px;width:355px;height:2px;background:linear-gradient(90deg,rgba(133,171,210,.2),var(--blue-soft),rgba(133,171,210,.2))}
  .tagline{position:absolute;left:44px;top:268px;font-size:35px;line-height:47px;font-weight:400;color:var(--blue-bright)}

  /* Steps band */
  .steps{position:absolute;left:0;top:459px;width:1038px;height:181px;background:linear-gradient(90deg,var(--blue-bright),var(--blue-mid) 55%,var(--blue-deep));box-shadow:0 8px 10px -6px rgba(0,0,0,.35)}
  .step{position:absolute;top:40px;display:flex;align-items:flex-start;gap:16px}
  .step-badge{width:98px;height:98px;border-radius:50%;border:4px solid var(--white);background:linear-gradient(180deg,var(--blue-bright),var(--blue-mid));display:flex;align-items:center;justify-content:center;flex:none;box-shadow:0 6px 8px rgba(0,0,0,.2)}
  .step-badge .equation{color:var(--white);font-size:16px;white-space:nowrap}
  .step-copy{padding-top:4px}
  .step-title{font-weight:600;font-size:22px;color:var(--white);margin-bottom:4px}
  .step-text{font-size:18px;line-height:26px;color:var(--blue-pale)}
  .step-1{left:34px}
  .step-2{left:310px}
  .step-3{left:662px}

  /* Details */
  .details{position:absolute;left:43px;top:696px;width:524px}
  .detail{border-bottom:2px solid var(--rule);padding-bottom:6px;margin-bottom:8px}
  .detail h3{font-weight:400;font-size:20px;color:var(--blue-deep);line-height:27px}
  .detail p{font-size:18.5px;line-height:24px;color:var(--text)}
  .plan-tag{position:absolute;left:43px;top:968px;width:252px;height:29px;background:var(--blue-deep);clip-path:polygon(0 0,96% 0,100% 100%,0 100%);color:var(--white);font-weight:600;font-size:18px;line-height:29px;padding-left:12px}
  .plan-list{position:absolute;left:43px;top:1000px;list-style:none}
  .plan-list li{display:flex;align-items:center;gap:14px;font-size:22px;color:var(--text);height:36px}
  .tick{width:22px;height:22px;flex:none}

  .phone-photo{position:absolute;left:646px;top:705px}

  /* Footer */
  .footer-bar{position:absolute;left:0;top:1113px;width:740px;height:87px;background:var(--ink-footer)}
  .signup{position:absolute;left:45px;top:1141px;font-size:20.5px;line-height:30px;font-weight:600;color:var(--blue-bright)}
  .contact{position:absolute;left:700px;top:1078px;width:338px;height:122px;background:linear-gradient(90deg,var(--blue-bright),var(--blue-deep));clip-path:polygon(12px 0,100% 0,100% 100%,0 100%,0 30px)}
  .contact ul{list-style:none;padding:12px 0 0 24px}
  .contact li{display:flex;align-items:center;gap:10px;color:var(--white);font-size:19px;font-weight:600;line-height:34px;white-space:nowrap}
  .contact svg{flex:none}
</style>
</head>
<body>
<main class="flier">

  <section class="hero">
    <svg class="hero-photo" width="1038" height="459" role="img" aria-label="Photo of a smiling student leaning on school lockers, holding a phone, with a hallway behind">
      <defs>
        <linearGradient id="hallway" x1="0" y1="0" x2="1" y2="1">
          <stop offset="0" stop-color="#d8cfa0"/>
          <stop offset=".45" stop-color="#8f8b86"/>
          <stop offset="1" stop-color="#3d4a63"/>
        </linearGradient>
        <linearGradient id="shade" x1="0" y1="0" x2="1" y2="0">
          <stop offset="0" stop-color="#15181c"/>
          <stop offset="1" stop-color="#2c3138"/>
        </linearGradient>
      </defs>
      <rect width="1038" height="459" fill="url(#shade)"/>
      <polygon points="340,0 1038,0 1038,459 493,459" fill="url(#hallway)"/>
    </svg>
    <div class="brand"><span class="brand-dot"></span><span class="brand-name">Lantern Scholars</span></div>
    <div class="brand-rule"></div>
    <h1 class="tagline">Personalized tutoring<br>in math and science via<br>your mobile device</h1>
  </section>

  <section class="steps">
    <div class="step step-1">
      <div class="step-badge"><span class="equation">4 - 2x = 0</span></div>
      <div class="step-copy">
        <div class="step-title">STEP 1</div>
        <div class="step-text">Send tutors<br>your problem</div>
      </div>
    </div>
    <div class="step step-2">
      <div class="step-badge">
        <svg width="56" height="46" viewBox="0 0 56 46">
          <path d="M22 4h26a6 6 0 0 1 6 6v14a6 6 0 0 1-6 6h-2l2 8-10-8H22" fill="#fff" opacity=".85"/>
          <path d="M6 10h26a6 6 0 0 1 6 6v14a6 6 0 0 1-6 6H18L8 44l2-8H6a6 6 0 0 1-6-6V16a6 6 0 0 1 6-6z" fill="#fff"/>
          <circle cx="11" cy="23" r="2.6" fill="#0492cd"/><circle cx="19" cy="23" r="2.6" fill="#0492cd"/><circle cx="27" cy="23" r="2.6" fill="#0492cd"/>
        </svg>
      </div>
      <div class="step-copy">
        <div class="step-title">STEP 2</div>
        <div class="step-text">Tutor sends response<br>to set up session</div>
      </div>
    </div>
    <div class="step step-3">
      <div class="step-badge">
        <svg width="54" height="46" viewBox="0 0 54 46">
          <rect x="2" y="2" width="50" height="34" rx="3" fill="none" stroke="#fff" stroke-width="4"/>
          <rect x="9" y="9" width="36" height="20" fill="#fff"/>
          <rect x="22" y="36" width="10" height="6" fill="#fff"/>
          <rect x="14" y="42" width="26" height="3" fill="#fff"/>
        </svg>
      </div>
      <div class="step-copy">
        <div class="step-title">STEP 3</div>
        <div class="step-text">Perform tutoring session and<br>receive copy of your notes!</div>
      </div>
    </div>
  </section>

  <section class="details">
    <div class="detail">
      <h3>Subjects Covered up to AP Courses</h3>
      <p>Math, Chemistry, Biology, Physics, ACT/SAT Prep</p>
    </div>
    <div class="detail">
      <h3>Our Tutors are Local Experts</h3>
      <p>Each Lantern Scholars tutor has or is pursing a PhD in a math, science, engineering, or medicine field.</p>
    </div>
    <div class="detail">
      <h3>No Scheduling Required!</h3>
      <p>Tutors will respond to set up a study session as soon as a student messages for help.</p>
    </div>
  </section>

  <div class="plan-tag">PAYMENT PLAN</div>
  <ul class="plan-list">
    <li><svg class="tick" viewBox="0 0 22 22"><rect width="22" height="22" rx="3" fill="#1a73c2"/><path d="M5 11l4 4 8-9" stroke="#fff" stroke-width="3" fill="none"/></svg>$150 for One Month Unlimited Sessions.</li>
    <li><svg class="tick" viewBox="0 0 22 22"><rect width="22" height="22" rx="3" fill="#1a73c2"/><path d="M5 11l4 4 8-9" stroke="#fff" stroke-width="3" fill="none"/></svg>First Tutoring Session is Free!</li>
  </ul>

  <svg class="phone-photo" width="380" height="370" role="img" aria-label="Photo of a hand holding a smartphone showing a handwritten triangle math problem">
    <defs>
      <radialGradient id="handGlow" cx=".5" cy=".5" r=".55">
        <stop offset="0" stop-color="#d9c2ad"/>
        <stop offset=".6" stop-color="#e6e2de"/>
        <stop offset="1" stop-color="#f3f3f3"/>
      </radialGradient>
    </defs>
    <rect width="380" height="370" fill="url(#handGlow)"/>
  </svg>

  <div class="footer-bar"></div>
  <p class="signup">Click here to sign up for your first, FREE tutoring session</p>

  <aside class="contact">
    <ul>
      <li><svg width="16" height="16" viewBox="0 0 16 16"><path d="M3 1l3 3-2 2a9 9 0 0 0 6 6l2-2 3 3-2 2C7 15 1 9 1 3z" fill="#fff"/></svg>866-555-0142</li>
      <li><svg width="16" height="12" viewBox="0 0 16 12"><rect x="0.5" y="0.5" width="15" height="11" fill="none" stroke="#fff"/><path d="M1 1l7 6 7-6" stroke="#fff" fill="none"/></svg>tutor@lanternscholars.com</li>
      <li><svg width="16" height="16" viewBox="0 0 16 16"><circle cx="8" cy="8" r="7" fill="none" stroke="#fff" stroke-width="1.4"/><ellipse cx="8" cy="8" rx="3" ry="7" fill="none" stroke="#fff" stroke-width="1.2"/><path d="M1 8h14" stroke="#fff" stroke-width="1.2"/></svg>lanternscholars.com</li>
    </ul>
  </aside>

</main>
</body>
</html>
```